Life Coaching business needs a new flyer

We are an Australian business that specialises in Life Coaching, Career Coaching, Health and Wellness Coaching, Yoga and Pilates. We need a A4 double sided flyer that is full colour and folded to DL format. I have attached a couple of designs that I like and some pictures and would like the flyer to be bright yet stylish.

Life Coaching

```html
<!DOCTYPE html>
<html lang="en">
<head>
<meta charset="utf-8">
<title>Clearpath Coaching – Inside Spread</title>
<link href="https://fonts.googleapis.com/css2?family=Crimson+Text:ital,wght@0,400;0,600;0,700;1,400&display=swap" rel="stylesheet">
<style>
  :root{
    --navy:#16408c;
    --blue:#1f6fbf;
    --sky:#4ea6de;
    --green:#7cc242;
    --deep-green:#3f9a3a;
    --ink:#2b2b2b;
    --white:#ffffff;
    --bg:#ffffff;
  }
  *{box-sizing:border-box;margin:0;padding:0}
  html,body{width:1200px;height:851px;overflow:hidden;background:var(--bg)}
  body{font-family:"Crimson Text",Georgia,serif;color:var(--ink)}
  .spread{position:relative;width:1200px;height:851px;overflow:hidden;background:var(--white)}
  .backdrop{position:absolute;inset:0}
  .photo{position:absolute}
  .photo.round{border-radius:50%;border:4px solid var(--white);box-shadow:0 2px 6px rgba(0,0,0,.15)}
  .copy{position:absolute}
  h2{font-weight:700;color:var(--blue);font-size:21px;line-height:1.05;margin-bottom:4px}
  p{font-size:14.5px;line-height:1.18;margin-bottom:5px}
  .questions p{color:var(--white);font-size:19px;line-height:1.05;margin-bottom:6px}
  .side h2{font-size:19px;margin-bottom:3px}
  .side p{font-size:13px;line-height:1.15;margin-bottom:4px}
  .issues{list-style:none;font-size:13px;line-height:1.15;margin-bottom:8px}
  .issues li{padding-left:10px;text-indent:-10px}
  .issues li::before{content:"•";color:var(--navy);margin-right:5px}
  .brand{position:absolute;display:flex;align-items:center;gap:10px}
  .brand-dot{width:38px;height:38px;border-radius:50%;background:var(--deep-green)}
  .brand-name{font-size:24px;font-weight:600;color:var(--blue);line-height:1}
  .fold{position:absolute;top:0;bottom:0;width:1px;background:rgba(0,0,0,.06)}
</style>
</head>
<body>
<main class="spread">
  <svg class="backdrop" width="1200" height="851" viewBox="0 0 1200 851" aria-hidden="true">
    <defs>
      <linearGradient id="deepBlue" x1="0" y1="0" x2="1" y2="1">
        <stop offset="0" stop-color="#1b4a98"/>
        <stop offset="1" stop-color="#2f87cc"/>
      </linearGradient>
      <linearGradient id="bandBlue" x1="0" y1="1" x2="1" y2="0">
        <stop offset="0" stop-color="#1c5fb0"/>
        <stop offset="1" stop-color="#3ea0dd"/>
      </linearGradient>
    </defs>
    <path d="M0 0 H400 V320 C330 400 200 430 0 405 Z" fill="url(#deepBlue)"/>
    <path d="M0 405 C200 430 330 400 400 320 V345 C330 425 200 452 0 428 Z" fill="#4ea6de"/>
    <path d="M300 0 H400 V100 C375 55 340 20 300 0 Z" fill="#7cc242"/>
    <path d="M400 20 C440 40 470 60 480 80 C455 60 430 45 400 40 Z" fill="#7cc242"/>
    <path d="M400 851 V795 C620 775 860 740 1200 665 V851 Z" fill="#7cc242"/>
    <path d="M400 851 V812 C630 795 870 762 1200 690 V851 Z" fill="url(#bandBlue)"/>
    <path d="M1080 0 H1200 V260 C1180 150 1140 60 1080 0 Z" fill="#7cc242"/>
    <path d="M1120 0 H1200 V120 C1180 70 1155 30 1120 0 Z" fill="#2f87cc"/>
  </svg>

  <div class="fold" style="left:400px"></div>
  <div class="fold" style="left:800px"></div>

  <!-- Left panel -->
  <section class="copy questions" style="left:28px;top:28px;width:280px">
    <p>Are you looking at making changes this year?</p>
    <p>Are you stuck in a rut or at a crossroad in your life?</p>
    <p>Are you wanting to lose weight but can't get motivated?</p>
    <p>Do you have ongoing problems with your career, relationships, or just life itself?</p>
    <p>Coaching is the answer</p>
  </section>
  <div class="photo round" role="img" aria-label="Photo of a woman relaxing on a pink float in a pool"
       style="left:262px;top:262px;width:136px;height:136px;background:linear-gradient(135deg,#3fb3d8,#e0487a 55%,#2a8fc4)"></div>

  <section class="copy" style="left:28px;top:450px;width:350px">
    <h2>Clearpath Coaching and Meditation Centre</h2>
    <p>Our mission is to help you become the best possible person you can be. Mentally, physically, and spiritually.</p>
    <p>We offer highly qualified and compassionate trainers/coaches for Life Coaching, Meditation, Yoga and Pilates.</p>
    <p>They will guide and motivate you every step of the way to achieve all your dreams and goals.</p>
    <p>They will make you be the best you can be</p>
  </section>
  <div class="photo" role="img" aria-label="Photo of a woman in a yoga pose on a beach by the sea"
       style="left:0;top:650px;width:400px;height:201px;background:linear-gradient(180deg,#8fd0f0,#d8f0fb 60%,#f4fbff)"></div>

  <!-- Middle panel -->
  <section class="copy" style="left:430px;top:40px;width:345px">
    <h2>Life Coaching</h2>
    <p>Your Life Coach will give you the confidence and the ability to move forward in a positive manner in all areas of your life where you crave change. Life Coaching is about breaking down the barriers preventing this change from happening, and creating the ideal environment for positive action to take place. It is a holistic approach, which looks at the present and sets goals for a totally successful future.</p>
    <h2 style="margin-top:14px">Career Coaching</h2>
    <p>Are you at a crossroads in your career and at a loss about what to do next? Do you want your work to be in alignment with the authentic you? It can be difficult to assess career options, goals, and strategies, and have the confidence to implement changes on your own. With the right coaching support, you will gain the clarity that you need to take control and have a fulfilling and rewarding career.</p>
    <h2 style="margin-top:14px">Wellness Coaching</h2>
    <p>Health and wellness coaches help their clients find the motivation and tools to achieve their health and wellness goals, working with the client to examine and improve the psychological framework that supports those goals.</p>
  </section>
  <div class="brand" style="left:470px;top:560px">
    <span class="brand-dot"></span>
    <span class="brand-name">Clearpath Coaching</span>
  </div>
  <div class="photo round" role="img" aria-label="Photo of a smiling office team"
       style="left:410px;top:700px;width:124px;height:124px;background:linear-gradient(135deg,#f2f2f2,#c9d6e2)"></div>
  <div class="photo round" role="img" aria-label="Photo of a senior couple on a boat"
       style="left:548px;top:630px;width:150px;height:150px;background:linear-gradient(135deg,#9fd2ef,#e8eef2 60%,#4b85b8)"></div>

  <!-- Right panel -->
  <section class="copy side" style="left:828px;top:28px;width:212px">
    <h2>Why Would I Need Help?</h2>
    <p>Coaching is for anyone who wants to make lasting changes in their life.</p>
    <h2 style="margin-top:8px">Coaching can assist with such issues as:</h2>
    <ul class="issues">
      <li>Creating a better work–life balance</li>
      <li>Resolving relationship issues</li>
      <li>Career guidance</li>
      <li>Stress management</li>
      <li>Weight loss and fitness</li>
      <li>Motivation and goal setting</li>
      <li>Boosting your self esteem</li>
      <li>Overcoming negative emotions and thoughts</li>
      <li>Better time management</li>
    </ul>
    <h2>Meditation</h2>
    <p>We specialise in teaching meditation from beginners to advanced and teach a variety of techniques for stress reduction, peace of mind, stillness, and clarity.</p>
    <h2 style="margin-top:6px">Yoga/Pilates</h2>
    <p>Your highly qualified and experienced Yoga or Pilates instructor will come to you and create a fun and varied workout based on what you enjoy and what your goals are.</p>
  </section>
  <div class="photo" role="img" aria-label="Photo of a joyful young woman in a floral dress jumping with arms raised"
       style="left:1052px;top:300px;width:148px;height:330px;border-radius:70px 0 0 36px;background:linear-gradient(160deg,#f3d6c4,#e86aa8 50%,#7fd0e8)"></div>
  <div class="photo round" role="img" aria-label="Photo of a group of friends jumping on a beach"
       style="left:835px;top:690px;width:150px;height:150px;background:linear-gradient(180deg,#4aa4e0,#bfe4f7 60%,#e9d7b8)"></div>
  <div class="photo round" role="img" aria-label="Photo of a mother and daughter hugging"
       style="left:1010px;top:680px;width:120px;height:120px;background:linear-gradient(135deg,#f4d9a6,#e9a86f)"></div>
</main>
</body>
</html>
```